Intranet for company management ERP Style

We need a redesign for our Intranet webpage (Images, CSS), we have all the code and functionality ready and a basic design but it is not good looking. In order to meet our company standards this design has to be fully responsive and elegant, also should display the colors of the company: (#F17808 #EDAA64 #F4B947 #F2A900 #292828 #3D3D3D #062953) usually Dark orange colors are the main ones, though we wouldn't mind to see other options or to implement a pair of skins that we could switch easily on the webpage.

Target Market(s)

this webpage is for internal use of the company but could also be sold to external customers in the future, our market is cryptocurrency and BPO

Industry/Entity Type

BPO, Cryptocurrency

Coding

Coded - Design and coding required

Number of Pages Required

1 page

Font styles to use
Other font styles liked:
• Headings: Montserrat Extra Bold, Sub headings: Montserrat, Text: Object Sans

Colors
F0912C
F2A743
F7CA91
FBE8D2
FDF5EE

Requirements
Nice to have
• elegant icons designs and menus

```html
<!DOCTYPE html>
<html lang="en">
<head>
<meta charset="utf-8">
<title>Meridian Hub Intranet – Suggestions</title>
<link href="https://fonts.googleapis.com/css2?family=IBM+Plex+Sans:wght@400;500;600&family=Montserrat:wght@600;700&display=swap" rel="stylesheet">
<style>
:root{
  --stage:#5a5a5c;
  --orange:#f0912c;
  --orange-deep:#f17808;
  --orange-soft:#f7ca91;
  --peach:#fdf5ee;
  --panel:#f5f3f3;
  --white:#ffffff;
  --ink:#292828;
  --ink-soft:#3d3d3d;
  --line:#d9d6d4;
  --sidebar-line:#e5872a;
}
*{box-sizing:border-box;margin:0;padding:0}
html,body{width:899px;height:1200px;overflow:hidden}
body{background:var(--stage);font-family:"IBM Plex Sans",sans-serif;color:var(--ink);position:relative}
.screen{position:absolute;left:78px;width:749px;background:var(--panel);overflow:hidden}
.screen--form{top:104px;height:526px}
.screen--list{top:684px;height:414px}
.sidebar{position:absolute;left:0;top:0;bottom:0;width:130px;background:var(--orange)}
.brand{position:absolute;left:16px;top:17px;display:flex;align-items:center;gap:8px}
.brand-dot{width:20px;height:20px;border-radius:50%;background:rgba(255,255,255,.35)}
.brand-name{font-family:"Montserrat",sans-serif;font-weight:700;font-size:12px;line-height:12px;color:var(--white);width:60px}
.nav{position:absolute;left:0;right:0;top:63px;list-style:none}
.nav li{height:36px;display:flex;align-items:center;padding-left:13px;gap:7px;border-bottom:1px solid var(--sidebar-line);font-family:"Montserrat",sans-serif;font-weight:700;font-size:8.7px;color:var(--white);letter-spacing:.2px}
.nav li:last-child{border-bottom:none}
.nav svg{width:10px;height:10px;fill:var(--white)}
.main{position:absolute;left:130px;right:0;top:0;bottom:0}
.topbar{height:23px;background:var(--white);border-bottom:1px solid #eee;position:relative}
.topbar svg{position:absolute;top:6px;width:9px;height:9px}
.topbar .tb-search{left:18px}
.topbar .tb-grid{left:36px}
.badge-icon{position:absolute;top:5px;width:12px;height:12px}
.badge-icon svg{position:static;width:11px;height:11px}
.badge{position:absolute;right:-3px;top:-2px;width:7px;height:7px;border-radius:50%;background:var(--orange);color:var(--white);font-size:5px;line-height:7px;text-align:center}
.avatar{position:absolute;right:5px;top:4px;width:14px;height:14px;border-radius:50%;background:var(--orange);overflow:hidden}
.page-head{height:39px;background:var(--white);padding:6px 0 0 13px;box-shadow:0 1px 2px rgba(0,0,0,.04)}
.page-title{font-size:11px;color:var(--orange);line-height:13px}
.crumbs{font-size:8px;color:var(--ink);margin-top:2px}
.card{position:absolute;background:var(--white)}
.screen--form .card{left:21px;top:81px;width:575px;height:401px}
.card-title{position:absolute;left:21px;top:19px;font-size:11px;font-weight:400}
.field{position:absolute;left:20px;width:535px;height:91px;border:1px solid #9a9a9a;padding:9px;font-size:7.6px}
.req{color:var(--orange)}
.country{position:absolute;top:355px;left:23px;height:28px;display:flex;align-items:center;font-size:7.6px}
.select{position:absolute;left:68px;top:355px;width:188px;height:28px;border:1px solid #9a9a9a;font-size:7.6px;padding:0 9px;display:flex;align-items:center;justify-content:space-between}
.select i{border:3px solid transparent;border-top:3px solid var(--ink);margin-top:3px}
.save{position:absolute;left:479px;top:355px;width:77px;height:28px;background:var(--orange);color:var(--white);font-weight:600;font-size:11px;letter-spacing:.5px;display:flex;align-items:center;justify-content:center}
.copyright{position:absolute;left:0;right:0;text-align:center;font-size:7.6px}
.screen--form .copyright{top:501px}
.screen--list .copyright{top:379px}
.screen--list .card{left:15px;top:81px;width:587px;height:273px}
.exports{position:absolute;left:19px;top:17px;display:flex;gap:5px}
.exports span{width:36px;height:16px;background:var(--orange);color:var(--white);font-size:7.2px;font-weight:600;display:flex;align-items:center;justify-content:center;letter-spacing:.3px}
.table{position:absolute;left:18px;top:43px;width:552px;border:1px solid #e4e0dd;border-collapse:collapse;font-size:7.6px}
.table th{height:23px;background:var(--peach);font-weight:400;text-align:left;padding-left:11px;border-left:1px solid #e4e0dd}
.table td{height:27.4px;padding-left:11px;color:var(--ink-soft);border-left:1px solid #e4e0dd}
.table tr:nth-child(even) td{background:#f7f6f6}
.table .date{text-align:center;padding-left:0}
.table td.date{text-align:left;padding-left:11px;word-spacing:5px}
.table tbody tr:first-child td{padding-top:4px}
.table tbody tr:last-child td{padding-bottom:6px}
.showing{position:absolute;left:19px;top:235px;font-size:7.6px;color:var(--ink-soft)}
.pager{position:absolute;top:231px;left:428px;display:flex;align-items:center;font-size:6.8px}
.pager .pg-btn{height:20px;border:1px solid var(--orange-soft);color:var(--orange);display:flex;align-items:center;justify-content:center}
.pager .prev{width:41px}
.pager .next{width:29px;margin-left:8px}
.pager .current{width:18px;height:20px;background:var(--orange);color:var(--white);display:flex;align-items:center;justify-content:center;margin-left:4px}
.pager .num{margin-left:7px;color:var(--ink)}
</style>
</head>
<body>

<!-- Form screen -->
<section class="screen screen--form">
  <aside class="sidebar">
    <div class="brand"><span class="brand-dot"></span><span class="brand-name">Meridian Hub</span></div>
    <ul class="nav">
      <li><svg viewBox="0 0 10 10"><path d="M5 1 0 5h1.5v4h2.5V6.5h2V9h2.5V5H10z"/></svg>HOME</li>
      <li><svg viewBox="0 0 10 10"><path d="M1 2h5v1H2v5h5V5h1v4H1zM8 .5l1.5 1.5-4 4H4V4.5z"/></svg>REQUESTS</li>
      <li><svg viewBox="0 0 10 10"><path d="M0 1h1v7h9v1H0zM2 7l2-4 2 2 2-3 1 1v4z"/></svg>REPORTS</li>
      <li><svg viewBox="0 0 10 10"><path d="M5 1a4 4 0 0 0-4 4v3h2V5H2a3 3 0 0 1 6 0H7v3h2V5a4 4 0 0 0-4-4z"/></svg>HELPDESK</li>
      <li><svg viewBox="0 0 10 10"><path d="M2 2h6v4.5H2zm1 1v2.5h4V3zM0 7.5h10V9H0z"/></svg>PAYROLL</li>
      <li><svg viewBox="0 0 10 10"><path d="M2 1h6l2 4v4H0V5zm-.5 4H4l.5 1h1L6 5h2.5L7.5 2h-5z"/></svg>SUGGESTION BOX</li>
      <li><svg viewBox="0 0 10 10"><path d="M4 0h2l.3 1.4 1.2.7 1.4-.5 1 1.7-1.1 1v1.4l1.1 1-1 1.7-1.4-.5-1.2.7L6 10H4l-.3-1.4-1.2-.7-1.4.5-1-1.7 1.1-1V4.3L.1 3.3l1-1.7 1.4.5 1.2-.7zm1 3.3a1.7 1.7 0 1 0 0 3.4 1.7 1.7 0 0 0 0-3.4z"/></svg>ADMINSTRATOR</li>
    </ul>
  </aside>
  <div class="main">
    <header class="topbar">
      <svg class="tb-search" viewBox="0 0 10 10"><circle cx="4" cy="4" r="3" fill="none" stroke="#3d3d3d" stroke-width="1.4"/><path d="M6.3 6.3 9 9" stroke="#3d3d3d" stroke-width="1.6"/></svg>
      <svg class="tb-grid" viewBox="0 0 10 10" fill="#3d3d3d"><rect x="0" y="1" width="2.5" height="2"/><rect x="3.7" y="1" width="2.5" height="2"/><rect x="7.4" y="1" width="2.5" height="2"/><rect x="0" y="4" width="2.5" height="2"/><rect x="3.7" y="4" width="2.5" height="2"/><rect x="7.4" y="4" width="2.5" height="2"/><rect x="0" y="7" width="2.5" height="2"/><rect x="3.7" y="7" width="2.5" height="2"/><rect x="7.4" y="7" width="2.5" height="2"/></svg>
      <span class="badge-icon" style="right:57px"><svg viewBox="0 0 10 10" fill="#3d3d3d"><path d="M5 1C2.2 1 0 2.8 0 5c0 1.1.5 2 1.4 2.7L.8 9.5 3.2 8.5c.6.2 1.2.5 1.8.5 2.8 0 5-1.8 5-4S7.8 1 5 1z"/></svg><span class="badge">0</span></span>
      <span class="badge-icon" style="right:34px"><svg viewBox="0 0 10 10" fill="#3d3d3d"><path d="M0 2h10v6H0zm.8.8L5 5.6 9.2 2.8z" fill-rule="evenodd"/></svg><span class="badge">0</span></span>
      <span class="avatar"><svg viewBox="0 0 14 14" style="position:static;width:14px;height:14px"><circle cx="7" cy="5.3" r="2.4" fill="#fff"/><path d="M2.5 12a4.5 4 0 0 1 9 0z" fill="#fff"/></svg></span>
    </header>
    <div class="page-head">
      <h1 class="page-title">Suggestion</h1>
      <p class="crumbs">Home &nbsp;&gt;&nbsp; Add new Suggestion</p>
    </div>
    <div class="card">
      <h2 class="card-title">Add New Suggestion</h2>
      <div class="field" style="top:49px">Describe your suggestion<span class="req">*</span></div>
      <div class="field" style="top:149px">How would your suggestion help us?<span class="req">*</span></div>
      <div class="field" style="top:248px">Additional comment</div>
      <span class="country">Country</span>
      <div class="select">Select<i></i></div>
      <div class="save">SAVE</div>
    </div>
    <p class="copyright">Copyright © 2022 All Rights Reserved</p>
  </div>
</section>

<!-- List screen -->
<section class="screen screen--list">
  <aside class="sidebar">
    <div class="brand"><span class="brand-dot"></span><span class="brand-name">Meridian Hub</span></div>
    <ul class="nav">
      <li><svg viewBox="0 0 10 10"><path d="M5 1 0 5h1.5v4h2.5V6.5h2V9h2.5V5H10z"/></svg>HOME</li>
      <li><svg viewBox="0 0 10 10"><path d="M1 2h5v1H2v5h5V5h1v4H1zM8 .5l1.5 1.5-4 4H4V4.5z"/></svg>REQUESTS</li>
      <li><svg viewBox="0 0 10 10"><path d="M0 1h1v7h9v1H0zM2 7l2-4 2 2 2-3 1 1v4z"/></svg>REPORTS</li>
      <li><svg viewBox="0 0 10 10"><path d="M5 1a4 4 0 0 0-4 4v3h2V5H2a3 3 0 0 1 6 0H7v3h2V5a4 4 0 0 0-4-4z"/></svg>HELPDESK</li>
      <li><svg viewBox="0 0 10 10"><path d="M2 2h6v4.5H2zm1 1v2.5h4V3zM0 7.5h10V9H0z"/></svg>PAYROLL</li>
      <li><svg viewBox="0 0 10 10"><path d="M2 1h6l2 4v4H0V5zm-.5 4H4l.5 1h1L6 5h2.5L7.5 2h-5z"/></svg>SUGGESTION BOX</li>
      <li><svg viewBox="0 0 10 10"><path d="M4 0h2l.3 1.4 1.2.7 1.4-.5 1 1.7-1.1 1v1.4l1.1 1-1 1.7-1.4-.5-1.2.7L6 10H4l-.3-1.4-1.2-.7-1.4.5-1-1.7 1.1-1V4.3L.1 3.3l1-1.7 1.4.5 1.2-.7zm1 3.3a1.7 1.7 0 1 0 0 3.4 1.7 1.7 0 0 0 0-3.4z"/></svg>ADMINSTRATOR</li>
    </ul>
  </aside>
  <div class="main">
    <header class="topbar">
      <svg class="tb-search" viewBox="0 0 10 10"><circle cx="4" cy="4" r="3" fill="none" stroke="#3d3d3d" stroke-width="1.4"/><path d="M6.3 6.3 9 9" stroke="#3d3d3d" stroke-width="1.6"/></svg>
      <svg class="tb-grid" viewBox="0 0 10 10" fill="#3d3d3d"><rect x="0" y="1" width="2.5" height="2"/><rect x="3.7" y="1" width="2.5" height="2"/><rect x="7.4" y="1" width="2.5" height="2"/><rect x="0" y="4" width="2.5" height="2"/><rect x="3.7" y="4" width="2.5" height="2"/><rect x="7.4" y="4" width="2.5" height="2"/><rect x="0" y="7" width="2.5" height="2"/><rect x="3.7" y="7" width="2.5" height="2"/><rect x="7.4" y="7" width="2.5" height="2"/></svg>
      <span class="badge-icon" style="right:57px"><svg viewBox="0 0 10 10" fill="#3d3d3d"><path d="M5 1C2.2 1 0 2.8 0 5c0 1.1.5 2 1.4 2.7L.8 9.5 3.2 8.5c.6.2 1.2.5 1.8.5 2.8 0 5-1.8 5-4S7.8 1 5 1z"/></svg><span class="badge">0</span></span>
      <span class="badge-icon" style="right:34px"><svg viewBox="0 0 10 10" fill="#3d3d3d"><path d="M0 2h10v6H0zm.8.8L5 5.6 9.2 2.8z" fill-rule="evenodd"/></svg><span class="badge">0</span></span>
      <span class="avatar"><svg viewBox="0 0 14 14" style="position:static;width:14px;height:14px"><circle cx="7" cy="5.3" r="2.4" fill="#fff"/><path d="M2.5 12a4.5 4 0 0 1 9 0z" fill="#fff"/></svg></span>
    </header>
    <div class="page-head">
      <h1 class="page-title">Suggestion</h1>
      <p class="crumbs">Home &nbsp;&gt;&nbsp; Add new Suggestion</p>
    </div>
    <div class="card">
      <div class="exports"><span>COPY</span><span>CSV</span><span>EXCEL</span><span>PDF</span><span>PRINT</span></div>
      <table class="table">
        <colgroup><col style="width:69px"><col style="width:124px"><col style="width:118px"><col style="width:123px"><col style="width:118px"></colgroup>
        <thead><tr><th>User name</th><th style="padding-left:17px">Description</th><th>Suggestion Home</th><th>Comments</th><th class="date">Date</th></tr></thead>
        <tbody>
          <tr><td>Richard</td><td style="padding-left:14px">Lorem Ipsum is simply</td><td>Lorem Ipsum is simply</td><td>Lorem Ipsum is simply</td><td class="date">25 Nov 2022 08:15 PM</td></tr>
          <tr><td>Ferando</td><td style="padding-left:14px">There are many variations</td><td>There are many variations</td><td>There are many variations</td><td class="date">25 Nov 2022 08:15 PM</td></tr>
          <tr><td>Peter prem</td><td style="padding-left:14px">It is a long established fact</td><td>It is a long established fact</td><td>It is a long established fact</td><td class="date">25 Nov 2022 08:15 PM</td></tr>
          <tr><td>Super admin</td><td style="padding-left:14px">But I must explain to you</td><td>But I must explain to you</td><td>But I must explain to you</td><td class="date">25 Nov 2022 08:15 PM</td></tr>
          <tr><td>Stanly</td><td style="padding-left:14px">On the other hand, we</td><td>On the other hand, we</td><td>On the other hand, we</td><td class="date">25 Nov 2022 08:15 PM</td></tr>
        </tbody>
      </table>
      <p class="showing">Showing &nbsp;1 to 4 entries</p>
      <nav class="pager">
        <span class="pg-btn prev">Previous</span>
        <span class="current">1</span>
        <span class="num">2</span><span class="num" style="margin-left:5px">3</span><span class="num" style="margin-left:5px">4</span><span class="num" style="margin-left:5px">5</span>
        <span class="pg-btn next">Next</span>
      </nav>
    </div>
    <p class="copyright">Copyright © 2022 All Rights Reserved</p>
  </div>
</section>

</body>
</html>
```